Coral Beacon Stationery Design Project

I am looking for a suitable stationary design for my company Coral Beacon Pty Ltd (ACN 582 914 306).

The requirements can be better explained by visiting my website
"coral-beacon-trust.org"

I will be sending letters to Ministers of State and the Heads of Government Agencies so the theme needs to be formal and serious.

A theme with a shield or similar picking on the "guardian" concept would be appropriate

Target Market(s)

Ministers of State and Department Agency Heads and legal firms, the heads of Trustee Companies as well as Members of Coral Beacon

Industry/Entity Type

Government

Requirements
Must have
• Letterhead design is a priority - Business Card secondary

Must include tag line "Steady hands for every estate we tend" with a registered trade mark superscript at the end that is an R in a circle {Windows Alt +0174 on numeric keypad or Mac Option +R}.

Must include website address "Coral-Beacon-Trust.org" plus Email address "corbeacon@mailvessel.net

Company name "Coral Beacon Pty. Ltd." and Australian Company Number "ACN 582 914 306" needs to be shown more discretely

Address is "47 Finch Crescent, Marrowdale, 3291"
Nice to have
• A watermark is something to be considered

```html
<!DOCTYPE html>
<html lang="en">
<head>
<meta charset="utf-8">
<title>Coral Beacon Stationery</title>
<link href="https://fonts.googleapis.com/css2?family=Source+Sans+3:wght@400;600&display=swap" rel="stylesheet">
<style>
  :root {
    --backdrop: #cbcbcb;
    --paper: #ffffff;
    --ink: #141414;
    --card: #1d1d1d;
    --card-mark: #262626;
    --gold: #d6b23c;
    --white: #ffffff;
    --mark-faint: #f1f1f1;
  }
  * { box-sizing: border-box; margin: 0; padding: 0; }
  html, body {
    width: 1200px; height: 1200px; overflow: hidden;
    background: var(--backdrop);
    font-family: "Source Sans 3", "Myriad Pro", sans-serif;
  }
  .canvas { position: relative; width: 1200px; height: 1200px; }
  .reg { font-size: 0.6em; vertical-align: super; line-height: 0; margin-left: 1px; }

  /* Letterhead */
  .letterhead {
    position: absolute; left: 326px; top: 65px; width: 768px; height: 1082px;
    background: var(--paper); overflow: hidden;
  }
  .letterhead-watermark { position: absolute; left: 0; top: 0; }
  .letterhead-header { position: absolute; left: 0; top: 0; width: 768px; height: 240px; }
  .brand {
    position: absolute; display: flex; align-items: center; gap: 12px;
    color: var(--gold); font-weight: 400; white-space: nowrap;
  }
  .brand-dot { border-radius: 50%; background: var(--gold); flex: none; }
  .letterhead .brand { left: 26px; top: 22px; font-size: 40px; }
  .letterhead .brand-dot { width: 46px; height: 46px; }
  .letterhead-tagline {
    position: absolute; left: 22px; top: 100px;
    color: var(--white); font-size: 15px;
  }
  .letterhead-contact {
    position: absolute; right: 12px; top: 10px; text-align: right;
    color: var(--gold); font-size: 13px; line-height: 16px; font-style: normal;
  }
  .letterhead-footer {
    position: absolute; left: 326px; top: 1082px; width: 376px; height: 42px;
    background: var(--ink); border-radius: 0 12px 12px 0;
    color: var(--gold); font-size: 14.5px;
    display: flex; align-items: center; gap: 22px; padding-left: 16px;
  }

  /* Business cards */
  .card {
    position: absolute; left: 98px; width: 434px; height: 281px;
    background: var(--card); border-radius: 14px; overflow: hidden;
    box-shadow: 0 1px 3px rgba(0,0,0,0.35);
  }
  .card-front { top: 400px; }
  .card-back { top: 696px; height: 280px; }
  .card-watermark { position: absolute; left: 0; top: 0; }
  .card-front .brand {
    left: 0; right: 0; top: 100px; justify-content: center; font-size: 32px;
  }
  .card-front .brand-dot { width: 40px; height: 40px; }
  .card-tagline {
    position: absolute; left: 0; right: 0; top: 162px; text-align: center;
    color: var(--white); font-size: 11px;
  }
  .card-back-brand {
    position: absolute; left: 56px; top: 84px; width: 128px;
    display: flex; flex-direction: column; align-items: center; gap: 10px;
    color: var(--gold); font-size: 20px; white-space: nowrap;
  }
  .card-back-brand .brand-dot { width: 70px; height: 70px; }
  .card-person { position: absolute; left: 212px; top: 106px; color: var(--white); }
  .person-name { font-size: 21px; line-height: 26px; margin-bottom: 6px; }
  .person-line { font-size: 12px; line-height: 18px; }
</style>
</head>
<body>
<div class="canvas">

  <section class="letterhead">
    <svg class="letterhead-watermark" width="768" height="1082" viewBox="0 0 768 1082" aria-hidden="true">
      <circle cx="520" cy="640" r="370" fill="none" stroke="var(--mark-faint)" stroke-width="40"/>
    </svg>
    <svg class="letterhead-header" viewBox="0 0 768 240" aria-hidden="true">
      <defs>
        <linearGradient id="goldBand" x1="0" y1="0" x2="1" y2="0">
          <stop offset="0" stop-color="#f7dd6c"/>
          <stop offset="0.5" stop-color="#e8c548"/>
          <stop offset="1" stop-color="#b8901f"/>
        </linearGradient>
        <linearGradient id="inkFade" x1="0" y1="0" x2="0" y2="1">
          <stop offset="0" stop-color="#2a2a2a"/>
          <stop offset="1" stop-color="#070707"/>
        </linearGradient>
      </defs>
      <path d="M0 0 H768 V68 C560 72 430 170 300 212 C200 238 80 234 0 226 Z" fill="url(#goldBand)"/>
      <path d="M0 0 H768 V60 C560 62 420 150 300 190 C200 216 80 214 0 206 Z" fill="url(#inkFade)"/>
    </svg>
    <div class="brand"><span class="brand-dot"></span>Coral Beacon</div>
    <p class="letterhead-tagline">Steady hands for every estate we tend<span class="reg">®</span></p>
    <address class="letterhead-contact">
      47 Finch Crescent, Marrowdale, 3291<br>
      www.Coral-Beacon-Trust.org<br>
      corbeacon@mailvessel.net
    </address>
  </section>

  <footer class="letterhead-footer">
    <span>Coral Beacon Pty Ltd</span>
    <span>ACN 582 914 306</span>
  </footer>

  <article class="card card-front">
    <svg class="card-watermark" width="434" height="281" viewBox="0 0 434 281" aria-hidden="true">
      <circle cx="400" cy="180" r="170" fill="none" stroke="var(--card-mark)" stroke-width="18"/>
    </svg>
    <div class="brand"><span class="brand-dot"></span>Coral Beacon</div>
    <p class="card-tagline">Steady hands for every estate we tend<span class="reg">®</span></p>
  </article>

  <article class="card card-back">
    <svg class="card-watermark" width="434" height="280" viewBox="0 0 434 280" aria-hidden="true">
      <circle cx="400" cy="180" r="170" fill="none" stroke="var(--card-mark)" stroke-width="18"/>
    </svg>
    <div class="card-back-brand"><span class="brand-dot"></span>Coral Beacon</div>
    <div class="card-person">
      <p class="person-name">Personnel Name</p>
      <p class="person-line">www.Coral-Beacon-Trust.org</p>
      <p class="person-line">corbeacon@mailvessel.net</p>
    </div>
  </article>

</div>
</body>
</html>
```